KRT Design Business Card

I need to develop a business card for my real estate design and investment company. Something clean, classic and professional with a modern vibe.

Industry/Entity Type

Real Estate

Font styles to use
Serif
Sans Serif

```html
<!DOCTYPE html>
<html lang="en">
<head>
<meta charset="utf-8">
<title>KRT Design Business Card</title>
<link rel="stylesheet" href="https://fonts.googleapis.com/css2?family=Questrial&display=swap">
<style>
  :root {
    --stage: #7b7b7b;
    --card-dark: #363435;
    --card-light: #ffffff;
    --ink-light: #ffffff;
    --ink-dark: #1e1e1e;
    --ink-muted: #7a7778;
    --font-main: "Questrial", "Century Gothic", sans-serif;
  }
  html, body {
    margin: 0;
    padding: 0;
    overflow: hidden;
  }
  .stage {
    position: relative;
    width: 1200px;
    height: 848px;
    background: var(--stage);
    font-family: var(--font-main);
    overflow: hidden;
  }
  .card {
    position: absolute;
    top: 135px;
    width: 369px;
    height: 571px;
    box-shadow: 1px 1px 2px rgba(0, 0, 0, 0.25);
    text-align: center;
  }
  .card--front {
    left: 209px;
    background: var(--card-dark);
    color: var(--ink-light);
  }
  .card--back {
    left: 616px;
    background: var(--card-light);
    color: var(--ink-dark);
  }
  .brand {
    position: absolute;
    left: 0;
    right: 0;
  }
  .card--front .brand { top: 218px; }
  .card--back .brand { top: 82px; }
  .brand__name {
    display: block;
    font-size: 84px;
    line-height: 1;
    letter-spacing: 10px;
    font-weight: 400;
  }
  .brand__tagline {
    display: block;
    margin-top: 10px;
    font-size: 17px;
    letter-spacing: 0.2px;
  }
  .services {
    position: absolute;
    top: 321px;
    left: 0;
    right: 0;
    margin: 0;
    padding: 0;
    list-style: none;
    font-size: 16px;
    line-height: 20px;
    color: var(--ink-muted);
  }
  .contact {
    position: absolute;
    top: 476px;
    left: 0;
    right: 0;
    margin: 0;
    font-style: normal;
    font-size: 16px;
    line-height: 20px;
    color: var(--ink-dark);
  }
</style>
</head>
<body>
<main class="stage">
  <section class="card card--front">
    <div class="brand">
      <span class="brand__name">KRT</span>
      <span class="brand__tagline">Design and Productions</span>
    </div>
  </section>

  <section class="card card--back">
    <div class="brand">
      <span class="brand__name">KRT</span>
      <span class="brand__tagline">Design and Productions</span>
    </div>
    <ul class="services">
      <li>Brief overview of services</li>
      <li>or a bullet pointed</li>
      <li>list could go here:</li>
      <li>• First</li>
      <li>• Second</li>
      <li>• Third</li>
    </ul>
    <address class="contact">
      telephone number<br>
      Email address@address.com<br>
      www.krtdesign.com
    </address>
  </section>
</main>
</body>
</html>
```